Improving the design of the attached webpage jpg image

Make the page professional, but keep it simple. All elements on the page can be changed to anything you like EXCEPT the blue bar at the top of the page.

The two images are the same page.

The content on the page must all be there. Do not add new content.

The design needs to feel like a professional score report.

Industry/Entity Type

Education

Number of Pages Required

1 page

Colors

Designer to choose colors to be used in the design.

Requirements
Must have
• The blue bar color and the bars themselves at the top and bottom of the page. All the content on the page.

```html
<!DOCTYPE html>
<html lang="en">
<head>
<meta charset="utf-8">
<title>Clearpath Admissions Test Score Report</title>
<link href="https://fonts.googleapis.com/css2?family=Figtree:wght@400;500;600;700&display=swap" rel="stylesheet">
<style>
:root{
  --band:#4a7d93;
  --band-light:#5289a0;
  --tab:#386a80;
  --ink:#2f4852;
  --ink-soft:#3d5660;
  --muted:#8e9a9f;
  --line:#e3e6e8;
  --track:#dadada;
  --red:#e5391c;
  --orange:#e9861a;
  --green:#6cc551;
  --chart:#3d758c;
  --pill:#f0f2f2;
  --score-sub:#93b2ba;
}
*{box-sizing:border-box;margin:0;padding:0}
html,body{width:1130px;height:1200px;overflow:hidden;background:#fff}
body{font-family:"Figtree",sans-serif;color:var(--ink);position:relative}
.band{position:absolute;left:0;top:0;width:1130px;height:393px;background:var(--band);overflow:hidden}
.band .ring{position:absolute;border-radius:50%;background:rgba(255,255,255,.045)}
.report-card{position:absolute;left:117px;top:87px;width:897px;height:195px;background:#fff;border-radius:15px;box-shadow:0 22px 40px rgba(30,60,75,.35)}
.report-card h1{position:absolute;left:30px;top:26px;font-size:18.5px;font-weight:700;color:var(--ink)}
.meta{position:absolute;left:30px;top:63px;display:flex;align-items:center;font-size:10.5px;font-weight:600;color:var(--ink)}
.meta svg{margin-right:8px}
.meta .item{display:flex;align-items:center;margin-right:18px}
.summary{position:absolute;left:30px;top:100px;width:615px;font-size:10.4px;line-height:18px;color:#4a5458}
.divider-v{position:absolute;left:694px;top:33px;width:1px;height:130px;background:var(--line)}
.total{position:absolute;left:742px;top:28px;width:110px;text-align:center}
.total .dial{position:relative;width:110px;height:110px}
.total .dial span{position:absolute;inset:0;display:flex;align-items:center;justify-content:center;font-size:33px;font-weight:700;color:var(--red)}
.total .of{margin-top:14px;font-size:15px;font-weight:600;color:var(--score-sub)}
.tabs{position:absolute;left:117px;top:356px;display:flex;gap:6px}
.tab{width:220px;height:37px;display:flex;align-items:center;justify-content:center;font-size:12px;font-weight:600;color:#fff;background:var(--tab);border-radius:6px 6px 0 0}
.tab.active{background:#fff;color:var(--ink)}
.heading{position:absolute;left:117px;display:flex;align-items:center;font-size:19.5px;font-weight:500;color:var(--ink-soft)}
.heading svg{margin-right:11px}
.table-head{position:absolute;top:536px;font-size:12px;font-weight:500;color:var(--muted)}
.rule{position:absolute;left:117px;width:896px;height:1px;background:var(--line)}
.row-label{position:absolute;left:117px;font-size:12px;font-weight:600;color:var(--ink)}
.pill{position:absolute;left:409px;height:26px;padding:0 15px;border-radius:13px;background:var(--pill);font-size:12px;display:flex;align-items:center;color:var(--ink)}
.meter{position:absolute;left:622px;width:391px;height:30px}
.meter .track{position:absolute;left:0;right:0;top:19px;height:5px;border-radius:3px;background:var(--track)}
.meter .fill{position:absolute;left:0;top:19px;height:5px;border-radius:3px}
.meter .tick{position:absolute;top:14px;width:1px;height:15px;background:#c8c8c8}
.meter .lbl{position:absolute;top:0;font-size:10px;color:var(--muted);transform:translateX(-50%)}
.meter .lbl.start{transform:none}
.meter .lbl.end{transform:none;right:0}
.meter .marker{position:absolute;top:12px;height:18px;min-width:28px;padding:0 7px;border-radius:9px;font-size:10px;font-weight:600;color:#fff;display:flex;align-items:center;justify-content:center;transform:translateX(-50%)}
.red{background:var(--red)}.orange{background:var(--orange)}.green{background:var(--green)}
.chart{position:absolute;left:110px;top:940px;width:910px;height:190px}
.chart .ylab{position:absolute;left:0;width:34px;text-align:right;font-size:10px;color:var(--muted);transform:translateY(-50%)}
.chart .grid{position:absolute;left:52px;width:851px;height:1px;background:#e9ebec}
.chart .bar{position:absolute;width:37px;background:var(--chart)}
.chart .xlab{position:absolute;top:167px;width:37px;text-align:center;font-size:10px;color:var(--muted)}
</style>
</head>
<body>
<header class="band">
  <div class="ring" style="left:70px;top:-430px;width:990px;height:990px"></div>
  <div class="ring" style="left:258px;top:-240px;width:614px;height:614px"></div>
</header>

<section class="report-card">
  <h1>Clearpath Admissions Test Score Report</h1>
  <div class="meta">
    <div class="item">
      <svg width="14" height="15" viewBox="0 0 14 15" fill="none" stroke="#8a9599" stroke-width="1"><rect x="1" y="2.5" width="12" height="11.5" rx="1"/><path d="M1 5.5h12M4 1v3M10 1v3"/><path d="M4 8h1M6.5 8h1M9 8h1M4 10.5h1M6.5 10.5h1M9 10.5h1"/></svg>
      September 4, 2024
    </div>
    <div class="item">
      <svg width="12" height="15" viewBox="0 0 12 15" fill="none" stroke="#8a9599" stroke-width="1"><path d="M1 1h6.5L11 4.5V14H1z"/><path d="M7.5 1v3.5H11M3.5 8h5M3.5 10.5h5"/></svg>
      Simulation test 2
    </div>
  </div>
  <p class="summary">From classic novels like "Northfield Manor" by Eleanor Whitby to contemporary bestsellers like "The Marlow Keys" by R.T. Vance, literature transcends time and culture, touching the hearts and minds of readers. The power of storytelling allows us to escape reality, gain empathy, and explore diverse perspectives, making literature an indispensable part of the human experience.</p>
  <div class="divider-v"></div>
  <div class="total">
    <div class="dial">
      <svg width="110" height="110" viewBox="0 0 110 110">
        <circle cx="55" cy="55" r="52" fill="none" stroke="#dcdcdc" stroke-width="3"/>
        <circle cx="55" cy="55" r="52" fill="none" stroke="var(--red)" stroke-width="3.5" stroke-dasharray="86 400" transform="rotate(-90 55 55)"/>
      </svg>
      <span>275</span>
    </div>
    <div class="of">275/805</div>
  </div>
</section>

<nav class="tabs">
  <div class="tab active">Overall performance</div>
  <div class="tab">Quantitative reasoning</div>
  <div class="tab">Verbal reasoning</div>
  <div class="tab">Data insights</div>
</nav>

<h2 class="heading" style="top:478px">
  <svg width="22" height="21" viewBox="0 0 24 23"><path fill="var(--chart)" d="M12 0l3.6 7.5 8.2 1.1-6 5.7 1.5 8.2L12 18.6 4.7 22.5l1.5-8.2-6-5.7 8.2-1.1z"/></svg>
  Section performance
</h2>

<div class="table-head" style="left:117px">Section</div>
<div class="table-head" style="left:408px">Percentile</div>
<div class="table-head" style="left:620px">Score</div>
<div class="rule" style="top:563px"></div>

<div class="row-label" style="top:594px">Overall performance</div>
<div class="pill" style="top:589px">1th</div>
<div class="meter" style="top:585px">
  <span class="lbl start" style="left:0">205</span><span class="lbl" style="left:64%">546</span><span class="lbl end">805</span>
  <div class="track"></div><div class="tick" style="left:64%"></div>
  <div class="fill red" style="width:31.1%"></div>
  <div class="marker red" style="left:31.1%">275</div>
</div>

<div class="row-label" style="top:648px">Quantitative reasoning</div>
<div class="pill" style="top:643px">2th</div>
<div class="meter" style="top:639px">
  <span class="lbl start" style="left:0">60</span><span class="lbl" style="left:64%">78</span><span class="lbl end">90</span>
  <div class="track"></div><div class="tick" style="left:64%"></div>
  <div class="fill red" style="width:26.7%"></div>
  <div class="marker red" style="left:26.7%">63</div>
</div>

<div class="row-label" style="top:702px">Verbal reasoning</div>
<div class="pill" style="top:697px">1th</div>
<div class="meter" style="top:693px">
  <span class="lbl start" style="left:0">60</span><span class="lbl" style="left:60.5%">75</span><span class="lbl end">90</span>
  <div class="track"></div><div class="tick" style="left:60.5%"></div>
  <div class="fill orange" style="width:51.7%"></div>
  <div class="marker orange" style="left:51.7%">65</div>
</div>

<div class="row-label" style="top:756px">Data insights</div>
<div class="pill" style="top:751px">5th</div>
<div class="meter" style="top:747px">
  <span class="lbl start" style="left:0">60</span><span class="lbl" style="left:55.7%">73</span><span class="lbl end">90</span>
  <div class="track"></div><div class="tick" style="left:55.7%"></div>
  <div class="fill green" style="width:79.6%"></div>
  <div class="marker green" style="left:79.6%">80</div>
</div>

<div class="rule" style="top:838px"></div>

<h2 class="heading" style="top:898px">
  <svg width="22" height="20" viewBox="0 0 24 22"><path fill="var(--chart)" d="M6 0h12v2h5v3c0 3.5-2.5 5.5-5.6 5.9C16.3 13 14.6 14.3 13 14.6V17h4v3H7v-3h4v-2.4c-1.6-.3-3.3-1.6-4.4-3.7C3.5 10.5 1 8.5 1 5V2h5zm-3 4v1c0 2 1.2 3.3 3 3.8V4zm18 0h-3v4.8c1.8-.5 3-1.8 3-3.8z"/></svg>
  Score distribution
</h2>

<div class="chart">
  <div class="ylab" style="top:13px">100%</div>
  <div class="ylab" style="top:48px">80%</div>
  <div class="ylab" style="top:83px">50%</div>
  <div class="ylab" style="top:118px">25%</div>
  <div class="ylab" style="top:154px">0</div>
  <div class="grid" style="top:9px"></div>
  <div class="grid" style="top:45px"></div>
  <div class="grid" style="top:81px"></div>
  <div class="grid" style="top:117px"></div>
  <div class="grid" style="top:154px"></div>
  <div class="bar" style="left:125px;top:24px;height:130px"></div>
  <div class="bar" style="left:287px;top:56px;height:98px"></div>
  <div class="bar" style="left:449px;top:100px;height:54px"></div>
  <div class="bar" style="left:612px;top:6px;height:148px"></div>
  <div class="bar" style="left:774px;top:6px;height:148px"></div>
  <div class="xlab" style="left:125px">1</div>
  <div class="xlab" style="left:287px">2</div>
  <div class="xlab" style="left:449px">3</div>
  <div class="xlab" style="left:612px">4</div>
  <div class="xlab" style="left:774px">5</div>
</div>
</body>
</html>
```